Webdesign für berufliches Schulzentrum für Ernährung, Gastgewerbe, Gesundheit
Zielgruppe
Berufliches Schulzentrum für Ernährung, Gastgewerbe, Gesundheit
Zielgruppe: Schüler und Auszubildende
Aufgabenstellung
- modernes, aber dennoch strukturiertes Aussehen der Webseite
- einfache Navigation
- die beiden Grüntöne aus dem Logo sollen sich bitte in der Seite wiederfinden - jedoch in freundlicher Form

```html
<!DOCTYPE html>
<html lang="de">
<head>
<meta charset="utf-8">
<title>Pläne und Termine – Schulzentrum Lindenau</title>
<link rel="stylesheet" href="https://fonts.googleapis.com/css2?family=Montserrat:wght@600;700&family=Heebo:wght@300;400;500&display=swap">
<style>
  :root {
    --bg: #f3f3f3;
    --page: #ffffff;
    --nav-bg: #f4f4f4;
    --ink: #2b2b2b;
    --ink-soft: #444;
    --green-dark: #1d4a2b;
    --green-mid: #4f7a60;
    --mint: #c5ecd2;
    --mint-strong: #b8e2c5;
    --line: #6d7a72;
  }
  * { margin: 0; padding: 0; box-sizing: border-box; }
  html, body { width: 1200px; height: 1200px; overflow: hidden; background: var(--bg); }
  .page {
    position: absolute; left: 0; top: 190px;
    width: 1200px; height: 821px;
    background: var(--page);
    font-family: "Heebo", Arial, sans-serif;
    color: var(--ink);
  }
  .site-header {
    position: relative; height: 90px; background: var(--nav-bg);
  }
  .brand {
    position: absolute; left: 19px; top: 0; width: 135px; height: 90px;
    display: flex; align-items: center; justify-content: center; gap: 6px;
    font-family: "Montserrat", Arial, sans-serif; font-weight: 700;
    font-size: 11px; letter-spacing: 1px; color: var(--green-dark); text-align: left; line-height: 1.3;
  }
  .brand-square { width: 12px; height: 12px; background: var(--green-dark); flex: none; }
  .main-nav a {
    position: absolute; top: 40px;
    font-family: "Montserrat", Arial, sans-serif; font-weight: 700;
    font-size: 9.5px; letter-spacing: 2px; color: var(--ink); text-decoration: none;
  }
  .main-nav a.is-active::after {
    content: ""; position: absolute; left: 0; bottom: -4px; width: 24px; height: 1.5px; background: var(--ink);
  }
  .menu-toggle { position: absolute; left: 1149px; top: 34px; }
  .hero {
    position: relative; height: 297px;
    background: linear-gradient(100deg, #8fb99d 0%, #6f9a7e 30%, #5f8669 60%, #2f5a3a 100%);
  }
  .hero-kicker {
    position: absolute; top: 71px; width: 100%; text-align: center;
    color: #fff; font-weight: 500; font-size: 15.5px; letter-spacing: 1px; padding-left: 20px;
  }
  .hero-title span {
    position: absolute; height: 56px; line-height: 56px; text-align: center;
    background: rgba(255,255,255,0.2); color: #fff;
    font-family: "Montserrat", Arial, sans-serif; font-weight: 600; font-size: 38px; letter-spacing: 6px;
  }
  .hero-title .line-1 { left: 472px; width: 240px; top: 103px; }
  .hero-title .line-2 { left: 314px; width: 562px; top: 171px; }
  .overview { position: relative; height: 421px; }
  .overview-title {
    position: absolute; top: 50px; width: 100%; text-align: center;
    font-weight: 400; font-size: 34px; letter-spacing: 4px; color: var(--ink);
  }
  .column-title {
    position: absolute; top: 154px; font-weight: 400; font-size: 24px; letter-spacing: 3px; color: var(--ink-soft);
  }
  .column-title.make-up { right: 679px; }
  .column-title.blocks { left: 668px; }
  .rule { position: absolute; top: 203px; height: 1px; background: var(--line); }
  .rule.left { left: 0; width: 521px; }
  .rule.right { left: 664px; right: 0; }
  .plan-button {
    position: absolute; width: 210px; height: 44px; line-height: 44px; text-align: center;
    background: var(--mint); color: var(--ink); font-weight: 500; font-size: 11.5px; letter-spacing: 2px;
    box-shadow: 2px 2px 3px rgba(90,120,160,0.35);
  }
  .plan-button.current { background: var(--mint-strong); }
  .footer-band { position: absolute; left: 0; bottom: 0; width: 100%; height: 13px; background: var(--green-dark); }
</style>
</head>
<body>
<div class="page">
  <header class="site-header">
    <div class="brand"><span class="brand-square"></span><span>Schulzentrum<br>Lindenau</span></div>
    <nav class="main-nav">
      <a style="left:196px">ÜBER UNS</a>
      <a style="left:294px">SCHULARTEN</a>
      <a class="is-active" style="left:415px">PLÄNE/TERMINE</a>
      <a style="left:555px">AKTUELLES</a>
      <a style="left:663px">SCHULANMELDUNG</a>
      <a style="left:815px">IMPRESSION</a>
      <a style="left:922px">FÖRDERVEREIN</a>
      <a style="left:1053px">KONTAKT</a>
    </nav>
    <svg class="menu-toggle" width="26" height="22" viewBox="0 0 26 22" aria-label="Menü">
      <g stroke="#2b2b2b" stroke-width="1.6"><line x1="1" y1="2" x2="25" y2="2"/><line x1="1" y1="11" x2="25" y2="11"/><line x1="1" y1="20" x2="25" y2="20"/></g>
    </svg>
  </header>
  <section class="hero" role="img" aria-label="Foto: Schülerin schreibt am Tisch, daneben Bücher und Stift, grün getönt">
    <p class="hero-kicker">Immer informiert!</p>
    <h1 class="hero-title"><span class="line-1">UNSERE</span><span class="line-2">PLÄNE UND TERMINE</span></h1>
  </section>
  <section class="overview">
    <h2 class="overview-title">Hier finden Sie:</h2>
    <h3 class="column-title make-up">Nachschreibetermine</h3>
    <h3 class="column-title blocks">Blockpläne</h3>
    <div class="rule left"></div>
    <div class="rule right"></div>
    <a class="plan-button" style="left:313px;top:231px">2. Halbjahr 2023/24</a>
    <a class="plan-button" style="left:313px;top:302px">1. Halbjahr 2023/24</a>
    <a class="plan-button current" style="left:664px;top:231px">2024/2025</a>
    <a class="plan-button" style="left:664px;top:302px">2023/2024</a>
    <div class="footer-band"></div>
  </section>
</div>
</body>
</html>
```